Small consulting business needs a website designed to highlight value and four offerings

My company is a dynamic consulting firm with four Core Offerings: Learning & Evaluation, Program Management, Facilitation & Coaching; Implementation & Transformation. Our mission is to facilitate organizational change and transformation, and to make space for creativity, joy, belonging, and trust. If done successfully, we grow to better understand ourselves, each other, and the work we do together.

I'd like the website to give a feeling of confidence and clarity. I want the colors to match or compliment my logo. I want to have three tabs - Our Clients, Our Services, and Government.

See attached Word document for additional content. My current website is www.BrightHarborGroup.com.

Some websites I'm inspired by:
https://www.quillmeadowworks.com
https://www.verolandpartners.com
https://tqvb.org

Some websites of people/groups in my field that I find uninspiring:
http://denisehollick.com
https://www.marrowfen.org

Target Market(s)

State and local government agencies, health tech, and corporate HR departments

Industry/Entity Type

public health, aging, government, health tech

Coding

Coded - Design and coding required

Number of Pages Required

4 page

Font styles to use
Other font styles liked:
• Calibri and Merriweather

Colors
0054AA
0677BA
7BADD7
CADEEF
E8F1F8
00AB8E
00BBA5
67D7C9
C6EFE9
E9F9F6
FFC000
F8CF3A
FAE287
FDF2CF
FEFAEE
F0912C
F2A743
F7CA91
FBE8D2
FDF5EE

Requirements
Must have
• Attached logo and content, water colors few, and photos.
Nice to have
• Real pictures, which I can provide to the chosen designer
Should not have
• AI generated characters or cartoons.

```html
<!DOCTYPE html>
<html lang="en">
<head>
<meta charset="utf-8">
<title>Bright Harbor Group</title>
<link href="https://fonts.googleapis.com/css2?family=Merriweather:wght@700;900&family=Montserrat:wght@400;500;600&display=swap" rel="stylesheet">
<style>
:root{
  --navy:#10284a;
  --text:#4a5563;
  --teal:#00AB8E;
  --teal-soft:#E9F9F6;
  --teal-mid:#C6EFE9;
  --yellow:#FFC000;
  --yellow-soft:#FEFAEE;
  --cream:#FDF2CF;
  --orange:#F0912C;
  --orange-soft:#FDF5EE;
  --line:#d9dde3;
  --white:#ffffff;
}
*{box-sizing:border-box;margin:0;padding:0}
html,body{width:1200px;height:3951px;overflow:hidden}
body{position:relative;background:var(--white);font-family:"Montserrat",sans-serif;color:var(--text);font-size:12px;line-height:1.65}
.abs{position:absolute}
h1,h2,h3,h4{font-family:"Merriweather",serif;color:var(--navy);font-weight:700}
.serif{font-family:"Merriweather",serif}
.center{text-align:center}
.btn{position:absolute;display:flex;align-items:center;justify-content:center;border:2px solid var(--orange);color:var(--orange);font-weight:600;font-size:12px;background:transparent;box-shadow:4px 4px 0 -1px var(--white),4px 4px 0 1px var(--orange)}

/* hero */
.hero-bg{left:0;top:0;width:1200px;height:561px;background:linear-gradient(100deg,#f5f4c2 0%,#dff3d6 35%,#c9f1ee 70%,#bff0f5 100%)}
.logo-box{left:150px;top:15px;width:108px;height:59px;background:var(--white);display:flex;align-items:center;gap:6px;padding:0 8px;font-family:"Merriweather",serif;font-size:9px;line-height:1.25;color:var(--navy)}
.logo-dot{width:14px;height:14px;border-radius:50%;background:var(--yellow);flex:none}
.nav{left:536px;top:34px;display:flex;gap:30px;font-size:13px;font-weight:600;color:var(--navy)}
.nav .active{color:var(--teal);border-bottom:2px solid var(--teal);padding-bottom:2px}
.nav-cta{left:940px;top:24px;width:106px;height:40px;font-size:13px}
.slide-label{top:288px;font-size:11px;color:#8aa0b6;letter-spacing:.5px}
.hero-title{left:149px;top:188px;width:480px;font-size:38px;line-height:1.3}
.hero-copy{left:149px;top:346px;width:460px;font-size:12.5px;color:#2f3a48}
.hero-art{left:686px;top:118px;width:360px;height:360px;border-radius:50%;background:radial-gradient(circle at 40% 40%,#f3c24a 0%,#7fb59a 55%,#2f6f6a 100%)}

/* clients */
.clients{left:149px;top:540px;width:900px;height:122px;background:var(--white);border-top:2px solid var(--yellow);border-bottom:2px solid #f2dc8a;box-shadow:0 10px 24px rgba(16,40,74,.08)}
.clients-tag{left:9px;top:8px;width:175px;height:104px;background:var(--yellow);color:var(--white);font-family:"Merriweather",serif;font-weight:900;font-size:21px;line-height:1.15;padding:26px 16px}
.client-row{left:225px;top:0;height:118px;width:660px;display:flex;align-items:center;justify-content:space-between;font-family:"Merriweather",serif;font-weight:700;font-size:12px;color:#555b63}

/* intro */
.sec-title{left:0;width:1200px;text-align:center;font-size:32px}
.sec-copy{left:200px;width:800px;text-align:center;font-size:12.5px}
.intro-art{left:149px;top:886px;width:268px;height:299px;border-radius:8px;background:linear-gradient(135deg,#c6efe9,#f3d48a 60%,#6aa39a)}
.intro-art-2{left:291px;top:946px;width:196px;height:239px;border-radius:8px;background:radial-gradient(circle,#f2c04a 0%,#8fc3b0 60%,rgba(255,255,255,.9) 100%)}
.vision{left:550px;top:872px;width:499px;height:126px;background:var(--yellow-soft);border-radius:6px;overflow:hidden}
.vision-art{right:0;top:0;width:170px;height:126px;background:radial-gradient(circle at 50% 45%,#f0b94a 0%,#cfe6d8 60%,#e4f5f1 100%)}
.block h4{font-size:15px;margin-bottom:8px}
.block p{font-size:12px}
.rule{border-bottom:1px dashed #c9ced6}

/* offerings */
.offer{top:1443px;width:208px;height:262px;background:#f2faf8;border-radius:6px;text-align:center;padding:20px 14px}
.offer.raised{background:var(--white);box-shadow:0 6px 22px rgba(16,40,74,.12);top:1441px;height:265px}
.offer-icon{width:56px;height:56px;border-radius:50%;background:var(--teal-mid);margin:16px auto 18px;display:flex;align-items:center;justify-content:center}
.offer h4{font-size:12.5px;margin-bottom:6px}
.offer p{font-size:12px}
.offer .btn{left:40px;bottom:28px;width:126px;height:34px;font-size:12px}

/* why */
.why{left:149px;top:1797px;width:900px;height:339px;background:var(--white);border-radius:6px;box-shadow:0 6px 26px rgba(16,40,74,.08)}
.why h2{position:absolute;left:38px;top:40px;font-size:30px}
.why-copy{left:38px;top:100px;width:320px;font-size:12px}
.tile{width:224px;height:125px;background:var(--yellow-soft);border-radius:4px;padding:14px 12px}
.tile-head{display:flex;align-items:center;gap:10px;margin-bottom:10px}
.tile-dot{width:32px;height:32px;border-radius:50%;background:var(--yellow);flex:none;display:flex;align-items:center;justify-content:center}
.tile h4{font-size:11.5px}
.tile p{font-size:12px}

/* we help */
.help-bg{left:0;top:2227px;width:1200px;height:376px;background:linear-gradient(100deg,#fbe9a2 0%,#fdf6df 35%,#f3f8ee 60%,#cdf3ef 85%,#f2f6b8 100%)}
.help-art{left:400px;top:2200px;width:380px;height:330px;border-radius:50%;background:radial-gradient(circle,#e6b771 0%,rgba(230,183,113,.35) 50%,rgba(255,255,255,0) 72%)}
.pill-track{left:149px;top:2368px;width:900px;height:70px;overflow:hidden}
.pill{top:0;height:70px;background:var(--white);border-radius:4px;display:flex;align-items:center;padding:0 26px;font-size:16px;font-weight:500;color:var(--navy);white-space:nowrap}

/* collaborate */
.collab-copy{left:149px;top:2767px;width:480px;font-size:12px}
.tag{top:2925px;height:30px;padding:0 12px;background:var(--teal-soft);color:var(--navy);font-size:11px;font-weight:600;display:flex;align-items:center;border-radius:3px}
.collab-art{left:704px;top:2695px;width:268px;height:260px;background:radial-gradient(circle at 45% 45%,#cfc97a 0%,#7fb4ad 40%,#fbeecb 75%)}
.collab-art-2{left:901px;top:2794px;width:141px;height:161px;background:radial-gradient(circle,#f2c04a 0%,#5c9a8c 55%,#f6f8f8 75%)}

/* testimonials */
.quote{top:3175px;width:397px;height:231px;background:var(--yellow-soft);border:1px solid #f0e6c4;padding:30px 28px}
.quote p{font-size:12px}
.quote h5{font-family:"Merriweather",serif;color:var(--navy);font-size:13px;margin-top:14px}
.quote span{font-size:11.5px}
.quote-mark{right:60px;bottom:40px;width:54px;height:54px;background:var(--teal-mid);border-radius:4px}

/* newsletter + footer */
.footer-bg{left:0;top:3520px;width:1200px;height:431px;background:linear-gradient(180deg,#fff 0%,#fbfbe9 60%,#eef8c8 100%)}
.email{left:592px;top:3572px;width:457px;height:38px;border:1px solid #d3dbe3;background:#f4f7f9;padding:0 16px;display:flex;align-items:center;font-size:12px;color:#55606d}
.foot-brand{left:150px;top:3712px;display:flex;align-items:center;gap:14px;font-family:"Merriweather",serif;font-size:24px;line-height:1.3;color:var(--navy)}
.foot-brand .logo-dot{width:52px;height:52px}
.social{left:830px;top:3744px;display:flex;gap:18px;font-size:11px;font-weight:600;color:var(--navy)}
.foot-nav{left:153px;top:3840px;display:flex;gap:26px;font-size:12.5px;font-weight:600;color:var(--navy)}
.foot-line{left:140px;top:3891px;width:910px;border-top:1px solid #d8e2c4}
.copyright{left:149px;top:3912px;font-size:11.5px}
.legal{right:151px;top:3912px;font-size:11.5px;color:var(--teal)}
</style>
</head>
<body>

<!-- Hero -->
<div class="abs hero-bg" role="img" aria-label="Soft watercolour wash of a community gathering in yellow and aqua tones"></div>
<div class="abs logo-box"><span class="logo-dot"></span><span>Bright Harbor<br>Group</span></div>
<nav class="abs nav"><span class="active">Home</span><span>Our Story</span><span>Services</span><span>Clients</span><span>Government</span></nav>
<div class="btn nav-cta">Contact Us</div>
<div class="abs slide-label" style="left:23px">&larr; &nbsp;PREV</div>
<div class="abs slide-label" style="left:1120px">NEXT &nbsp;&rarr;</div>
<h1 class="abs hero-title">A Seat at the Table for Collaboration, Learning, and Meaningful Change.</h1>
<p class="abs hero-copy">Bright Harbor Group is a dynamic consulting firm with four Core Offerings: Learning &amp; Evaluation, Program Management, Facilitation &amp; Coaching; Implementation &amp; Transformation.</p>
<div class="abs hero-art" role="img" aria-label="Watercolour circle of interlocking puzzle pieces in gold and green"></div>

<!-- Clients -->
<div class="abs clients">
  <div class="abs clients-tag">Meet Our Clients</div>
  <div class="abs client-row">
    <span>Cindral</span><span>Quill Meadow</span><span>Tessan Health</span><span>Northvale</span><span>Orvane Health</span><span>Marrowfen</span>
  </div>
</div>

<!-- Intro -->
<h2 class="abs sec-title" style="top:746px">Introducing us</h2>
<p class="abs sec-copy" style="top:796px">Bright Harbor Group is a woman-owned business in Riverton, CA, supporting U.S. organizations, communities, and governments through strategic planning, facilitation, and programs that advance health equity and community well-being.</p>
<div class="abs intro-art" role="img" aria-label="Watercolour landscape with sun and flowing river"></div>
<div class="abs intro-art-2" role="img" aria-label="Watercolour knot of joined figures in a circle"></div>
<div class="abs vision">
  <div class="abs block" style="left:22px;top:20px;width:290px"><h4>Our Vision</h4><p>Our vision is a world where people connect as humans first, growing and evolving together through meaningful collaboration.</p></div>
  <div class="abs vision-art" role="img" aria-label="Watercolour sunrise over a path"></div>
</div>
<div class="abs block rule" style="left:550px;top:1024px;width:499px;padding-bottom:20px"><h4>Our Mission</h4><p>Our mission is to facilitate organizational change and transformation, and to make space for creativity, joy, belonging, and trust. If done successfully, we grow to better understand ourselves, each other, and the work we do together.</p></div>
<div class="abs block rule" style="left:554px;top:1140px;width:495px;padding-bottom:8px"><h4>Our Value</h4><p>We are your steady partner in chaos, driving lasting change through values realignment, expert support, and strategic planning for organizations ready to grow and innovate.</p></div>

<!-- Offerings -->
<h2 class="abs sec-title" style="top:1316px">Four Core Offering</h2>
<p class="abs sec-copy" style="top:1367px">Bright Harbor Group (Bright Harbor) is a values-driven partner with deep roots in multi-sector leadership, adult learning, facilitation, and systems transformation.</p>

<div class="abs offer" style="left:149px">
  <div class="offer-icon"><svg width="26" height="26" viewBox="0 0 26 26" fill="none" stroke="#00AB8E" stroke-width="1.6"><circle cx="13" cy="10" r="6"/><path d="M10 19h6M11 22h4"/></svg></div>
  <h4>Learning &amp; Evaluation</h4><p>Learning and Evaluation is BHG's chief offering. In order...</p>
  <div class="btn">Learn More</div>
</div>
<div class="abs offer" style="left:380px">
  <div class="offer-icon"><svg width="26" height="26" viewBox="0 0 26 26" fill="none" stroke="#00AB8E" stroke-width="1.6"><circle cx="13" cy="9" r="5"/><path d="M4 22c2-5 5-7 9-7s7 2 9 7"/></svg></div>
  <h4>Program Management</h4><p>Multi-Sector Program Management .Whether supp...</p>
  <div class="btn">Learn More</div>
</div>
<div class="abs offer" style="left:611px">
  <div class="offer-icon"><svg width="26" height="26" viewBox="0 0 26 26" fill="none" stroke="#00AB8E" stroke-width="1.6"><rect x="3" y="4" width="12" height="8" rx="1"/><path d="M9 12v6h10M19 14v8"/></svg></div>
  <h4>Facilitation &amp; Coaching</h4><p>Our team has a unique capacity for facilitating hone...</p>
  <div class="btn">Learn More</div>
</div>
<div class="abs offer raised" style="left:841px">
  <div class="offer-icon"><svg width="26" height="26" viewBox="0 0 26 26" fill="none" stroke="#00AB8E" stroke-width="1.6"><circle cx="9" cy="9" r="4"/><circle cx="18" cy="18" r="4"/><path d="M12 12l3 3"/></svg></div>
  <h4>Implementation &amp; Transformation</h4><p>BHG's Implementation &amp; Transformation Core Offerin...</p>
  <div class="btn" style="bottom:20px">Learn More</div>
</div>

<!-- Why us -->
<section class="abs why">
  <h2>Why Us</h2>
  <p class="abs why-copy">Through our Core Offerings and guided by our founder's traditional and nontraditional methods for engaging and steering a team, we create a sense of belonging, foster transparency, and help to build stronger relationships. Our approach helps to drive meaningful change so that organizations and initiatives can clear roadblocks and meet collective goals. Our team's proven ability to transform conflict into opportunity will help to advance your organization and the communities you serve.</p>
  <div class="abs tile" style="left:401px;top:36px"><div class="tile-head"><span class="tile-dot"><svg width="14" height="14" viewBox="0 0 14 14" fill="none" stroke="#fff" stroke-width="1.5"><rect x="2" y="2" width="10" height="8"/></svg></span><h4>Strategic &amp; Practical</h4></div><p>We turn vision into action with clear plans and practical support.</p></div>
  <div class="abs tile" style="left:640px;top:36px"><div class="tile-head"><span class="tile-dot"><svg width="14" height="14" viewBox="0 0 14 14" fill="none" stroke="#fff" stroke-width="1.5"><circle cx="7" cy="7" r="4"/></svg></span><h4>Community-Centered Approach</h4></div><p>We prioritize lived experience, local knowledge, and inclusive collaboration in every project.</p></div>
  <div class="abs tile" style="left:401px;top:177px"><div class="tile-head"><span class="tile-dot"><svg width="14" height="14" viewBox="0 0 14 14" fill="none" stroke="#fff" stroke-width="1.5"><path d="M7 2l5 10H2z"/></svg></span><h4>Interdisciplinary Expertise</h4></div><p>Our team blends expertise in public health, strategy, facilitation,planning.</p></div>
  <div class="abs tile" style="left:640px;top:177px"><div class="tile-head"><span class="tile-dot"><svg width="14" height="14" viewBox="0 0 14 14" fill="none" stroke="#fff" stroke-width="1.5"><circle cx="5" cy="7" r="3"/><circle cx="9" cy="7" r="3"/></svg></span><h4>Collaborative Spirit</h4></div><p>We co-create with partners to foster ownership, alignment, and lasting success.</p></div>
</section>

<!-- We help -->
<div class="abs help-bg" role="img" aria-label="Soft watercolour wash in yellow and aqua"></div>
<div class="abs help-art" role="img" aria-label="Faded watercolour globe"></div>
<h2 class="abs sec-title" style="top:2296px">We Help Your Team</h2>
<div class="abs pill-track">
  <div class="abs pill" style="left:-30px;width:304px">Transform conflict into opportunity.</div>
  <div class="abs pill" style="left:294px;width:376px">Turn bold visions into practical results.</div>
  <div class="abs pill" style="left:691px;width:330px">Foster a sense of belonging.</div>
</div>
<div class="btn" style="left:452px;top:2474px;width:292px;height:49px">Find Common Ground</div>

<!-- Collaborate -->
<h2 class="abs" style="left:149px;top:2708px;font-size:32px">We Collaborate With</h2>
<p class="abs collab-copy">Choose your own adventure with customized proposals and partnerships that help you and your team learn, strategize, and implement together. We can offer an array of services related to project design, management, facilitation, and implementation. Our team can support your learning and quality improvement goal along the way to help align intent with impact. We are a growing, passionate team looking for opportunities to imagine, create, and innovate with you.</p>
<div class="abs" style="left:147px;top:2929px;color:var(--teal);font-size:14px">&lsaquo;</div>
<div class="abs tag" style="left:170px">Large-scale Companies</div>
<div class="abs tag" style="left:344px">National and local nonprofits</div>
<div class="abs" style="left:547px;top:2929px;color:var(--teal);font-size:14px">&rsaquo;</div>
<div class="abs collab-art" role="img" aria-label="Watercolour of overlapping circles and branches"></div>
<div class="abs collab-art-2" role="img" aria-label="Watercolour puzzle circle"></div>

<!-- Testimonials -->
<h2 class="abs sec-title" style="top:3056px">What Our Customers Say</h2>
<p class="abs sec-copy" style="top:3106px">From engineers shaping the future to public health experts tackling community challenges, we help a wide range of clients achieve their goals.</p>
<div class="abs slide-label" style="left:110px;top:3284px;color:#f2a743">&larr; &nbsp;PREV</div>
<div class="abs slide-label" style="left:1032px;top:3284px;color:#f2a743">NEXT &nbsp;&rarr;</div>
<div class="abs quote" style="left:190px">
  <p>Bright Harbor Group is a phenomenal partner. Mara Ellison is exceptionally knowledgeable about the public health field and brings a collaborative spirit, skillful facilitation, cultural awareness, and meticulous project management to her work. I hope for many more opportunities to work with her.</p>
  <h5>Owen Tallis</h5><span>Marrowfen Policy Center</span>
  <div class="abs quote-mark"></div>
</div>
<div class="abs quote" style="left:610px">
  <p>Bright Harbor Group supported our strategic planning efforts early in our transition from bench research to business operations. Mara is great at helping visualize road maps and therefore planning what is realistic and achievable. We have benefited from the structures came out of engagement with her.</p>
  <h5>Arun Velkar, MSE</h5><span>Tessan Health</span>
  <div class="abs quote-mark"></div>
</div>

<!-- Newsletter & footer -->
<div class="abs footer-bg"></div>
<p class="abs" style="left:149px;top:3570px;width:370px;font-size:12px">Bright Harbor was created to bring something different to the table: a consulting model that leads with values, honors people's lived experience, and makes space for creativity and joy.</p>
<div class="abs email">Enter Email Address</div>
<div class="btn" style="left:592px;top:3624px;width:242px;height:52px;background:var(--yellow-soft)">SUBMIT NOW</div>
<div class="abs foot-brand"><span class="logo-dot"></span><span>Bright Harbor<br>&nbsp;&nbsp;Group</span></div>
<div class="abs social"><span>Share</span><span>Post</span><span>Watch</span><span>Photos</span><span>Connect</span></div>
<nav class="abs foot-nav"><span>HOME</span><span>OUR STORY</span><span>SERVICES</span><span>CLIENTS</span><span>GOVERNMENT</span><span>CONTACT US</span></nav>
<div class="abs foot-line"></div>
<div class="abs copyright">&copy; Copyright 2025 by Bright Harbor Group</div>
<div class="abs legal">Terms &amp; Conditions &nbsp; | &nbsp; Privacy Policy</div>

</body>
</html>
```